Business Card Design

We are a manufacturing company that has been in business for over 30 years, established in 1981. We are looking to increase our business with defence force, government, and the major telecoms so the card needs to present the company as being cutting edge, secure, and professional.
Industry/Entity Type
Defence
Contact Information for Business Card
Name Gregory Pell
Phone 02 9374 5086
Fax 02 9453 7061
mobile 0427386204
Email Greg@Korvex.com.au
Webiste www.korvex.com.au
ABN 48 006 517 392
address: 17 Tallow Street Ingleburn NSW 2565
"Manufacturer of Antennas, GPS, Microwave, Cable Assemblies, RF, Military, & Telecommunications"

```html
<!DOCTYPE html>
<html lang="en">
<head>
<meta charset="utf-8">
<title>Korvex Business Card</title>
<link href="https://fonts.googleapis.com/css2?family=Ubuntu:wght@400;500;700&display=swap" rel="stylesheet">
<style>
  :root {
    --canvas: #e4e4e2;
    --charcoal: #2e2d33;
    --charcoal-band: #252429;
    --rust: #a0421f;
    --paper: #ffffff;
    --ink: #1f1f22;
    --rule: #3a3a3e;
    --edge: #2a2a2c;
  }
  * { box-sizing: border-box; margin: 0; padding: 0; }
  html, body {
    width: 1200px; height: 1000px; overflow: hidden;
    background: var(--canvas);
    font-family: "Ubuntu", sans-serif;
  }
  .canvas { position: relative; width: 1200px; height: 1000px; }
  .card {
    position: absolute; left: 200px; width: 800px; height: 457px;
    overflow: hidden;
    box-shadow: 0 6px 18px rgba(0,0,0,.18);
  }
  /* Front */
  .card--front { top: 30px; background: var(--charcoal); }
  .front__stripe {
    position: absolute; left: 50px; top: 0; width: 240px; height: 100%;
    background: var(--rust);
  }
  .front__band {
    position: absolute; left: 290px; right: 0; top: 150px; height: 150px;
    background: var(--charcoal-band);
  }
  .front__name {
    position: absolute; left: 340px; top: 194px;
    color: var(--paper); font-weight: 700; font-size: 58px;
    letter-spacing: 10px; line-height: 1;
  }
  /* Back */
  .card--back { top: 513px; background: var(--paper); }
  .back__stripe {
    position: absolute; left: 30px; top: 0; width: 270px; height: 100%;
    background: var(--rust);
    display: flex; flex-direction: column; align-items: center;
    color: var(--paper); text-align: center;
  }
  .back__brand {
    margin-top: 70px; font-weight: 700; font-size: 40px; letter-spacing: 4px;
  }
  .back__tagline {
    margin-top: 70px; font-size: 16px; font-weight: 500; line-height: 1.9;
  }
  .back__edge {
    position: absolute; right: 0; top: 0; width: 52px; height: 100%;
    background: var(--edge);
  }
  .details {
    position: absolute; left: 330px; top: 34px; width: 380px; color: var(--ink);
  }
  .details__name {
    font-weight: 700; font-size: 27px; letter-spacing: 1px;
    padding: 12px 0 8px; border-top: 1.5px solid var(--rule);
    border-bottom: 1.5px solid var(--rule);
  }
  .details__address {
    display: flex; align-items: center; gap: 8px;
    font-size: 17px; padding: 18px 0 26px;
    border-bottom: 1.5px solid var(--rule);
  }
  .contact-list { list-style: none; padding-top: 22px; }
  .contact-list li {
    display: flex; align-items: center; gap: 10px;
    font-size: 20px; line-height: 1.45;
  }
  .icon { width: 16px; height: 16px; flex: none; fill: var(--ink); }
</style>
</head>
<body>
<main class="canvas">
  <section class="card card--front" aria-label="Card front">
    <div class="front__stripe"></div>
    <div class="front__band"></div>
    <h1 class="front__name">KORVEX</h1>
  </section>

  <section class="card card--back" aria-label="Card back">
    <div class="back__stripe">
      <div class="back__brand">KORVEX</div>
      <p class="back__tagline">Manufacturer of Antennas,<br>GPS, Microwave,<br>Cable Assemblies,<br>RF, Military, &amp;<br>Telecommunications</p>
    </div>
    <div class="back__edge"></div>
    <div class="details">
      <h2 class="details__name">GREGORY PELL</h2>
      <p class="details__address">
        <svg class="icon" viewBox="0 0 16 16"><path d="M8 1 0 8h2v7h4v-5h4v5h4V8h2z"/></svg>
        17 Tallow Street Marrick Vale NSW 2748
      </p>
      <ul class="contact-list">
        <li><svg class="icon" viewBox="0 0 16 16"><path d="M3 1l3 3-2 2c1 2 3 4 6 6l2-2 3 3-2 2C7 15 1 9 1 3z"/></svg>02 9374 5086</li>
        <li><svg class="icon" viewBox="0 0 16 16"><path d="M4 1h7v4H4zM1 6h14v7h-3v2H4v-2H1zM5 10v4h6v-4z"/></svg>02 9453 7061</li>
        <li><svg class="icon" viewBox="0 0 16 16"><path d="M4 0h8v16H4zM5 2v10h6V2z"/></svg>042 738 6204</li>
        <li><svg class="icon" viewBox="0 0 16 16"><path d="M0 3h16L8 9zM0 5l8 6 8-6v8H0z"/></svg>greg@korvex.com.au</li>
        <li><svg class="icon" viewBox="0 0 16 16"><path d="M10 1a5 5 0 1 1 0 10 5 5 0 0 1 0-10zm0 2a3 3 0 1 0 0 6 3 3 0 0 0 0-6zM6 10l1.5 1.5L2 16 0.5 14.5z"/></svg>www.korvex.com.au</li>
      </ul>
    </div>
  </section>
</main>
</body>
</html>
```